Business cards and Stationary | Lumora Music Events

Hello! We need business cards and stationery for a new small business in the music industry. "Lumora is a high-end music agency which provides an unparalleled level of talent and personalized service to the realm entertainment, corporate events, and luxury weddings. Here is where the classical meets the contemporary and we can bring your vision to life.Keeping a steady finger on the pulse of current trends and consistently raising the bar for industry standards, Lumora continues to rise to the forefront of the music industry, providing the utmost professional, high-end, elegant, and engaging entertainment in Australia and World-Wide."

Target Market(s)

Class A. high profile corporate business.

Industry/Entity Type

Entertainment

Contact Information for Business Card

Lumora Music Events

Clare Yoshinaga
Director | Violinist

Level 7, 41 Caddow Lane
Sydney, 2000

Website: www.lumoramusicevents-demo.net
Phone number: 0455 318 602
Email: clare@lumoramusicevents-demo.net

Font styles to use
Serif
Sans Serif
Script

Colors
feeeee
0355a3
f59296
ffffff

Requirements
Nice to have
• Clean and sophisticated would be perfect.
• If there is a way to include the Instagram without being tacky, that would be awesome
• @lumoramusicevents
• Our website and logo have the following fonts:
• The primary logo is inspired and based on a font called BillionScript but the B is completely hand drawn and the rest is customised a bit to work together cohesively
• Monserrat Light - Is the Music part of the logo and as headers in the site
• Open Sans 300 and 400 (Light or Regular) is used mostly as the body text in the site
• If you want to access the website:
• www.lumoramusicevents-demo.net
• username: client
• password: preview

```html
<!DOCTYPE html>
<html lang="en">
<head>
<meta charset="utf-8">
<title>Lumora Music Events – Business Cards</title>
<link href="https://fonts.googleapis.com/css2?family=Montserrat:wght@300&family=Open+Sans:wght@300;400;700&display=swap" rel="stylesheet">
<style>
  :root {
    --backdrop: #3a302b;
    --card: #1d1e20;
    --card-edge: #2a2b2e;
    --rose: #d8a39f;
    --ink: #f2f0ef;
    --muted: #8d8c8c;
  }
  * { box-sizing: border-box; margin: 0; padding: 0; }
  html, body { width: 1200px; height: 864px; overflow: hidden; }
  body {
    background: var(--backdrop);
    font-family: "Open Sans", sans-serif;
    position: relative;
  }
  .card {
    position: absolute;
    width: 540px;
    height: 309px;
    background: var(--card);
    border: 1px solid var(--card-edge);
    box-shadow: 0 14px 30px rgba(0,0,0,.45);
  }
  .card--back { left: 40px; top: 110px; }
  .card--front { left: 620px; top: 420px; }

  /* back */
  .back-mark {
    position: absolute; left: 0; right: 0; top: 110px;
    text-align: center;
    font-family: "Open Sans", sans-serif;
    font-weight: 300;
    font-size: 40px;
    letter-spacing: 3px;
    color: #3a3b3e;
  }
  .back-url {
    position: absolute; left: 0; right: 0; bottom: 40px;
    text-align: center;
    color: var(--ink);
    font-size: 13px;
    letter-spacing: 3px;
  }

  /* front */
  .brand {
    position: absolute; right: 40px; top: 70px;
    display: flex; align-items: center; gap: 10px;
    font-weight: 300;
    font-size: 30px;
    color: var(--rose);
    letter-spacing: 1px;
  }
  .brand-dot { width: 10px; height: 10px; border-radius: 50%; background: var(--rose); }

  .person { position: absolute; left: 34px; top: 66px; }
  .person-name { color: var(--rose); font-weight: 700; font-size: 17px; letter-spacing: .5px; }
  .person-role { color: var(--ink); font-size: 13px; letter-spacing: .5px; margin-top: 1px; }

  .contacts { position: absolute; left: 34px; top: 118px; list-style: none; }
  .contacts li {
    display: flex; align-items: center; gap: 8px;
    color: var(--ink); font-size: 13px; line-height: 19px;
  }
  .contacts svg { width: 12px; height: 12px; fill: var(--rose); flex: none; }

  .divider {
    position: absolute; left: 34px; right: 34px; top: 200px;
    height: 1px; background: var(--ink);
  }

  .address {
    position: absolute; right: 34px; top: 214px;
    text-align: right; color: var(--ink); font-size: 13px; line-height: 19px;
  }
</style>
</head>
<body>

<section class="card card--back" aria-label="Business card, back">
  <div class="back-mark">Lumora Music</div>
  <p class="back-url">www.lumoramusicevents-demo.net</p>
</section>

<section class="card card--front" aria-label="Business card, front">
  <div class="brand"><span class="brand-dot"></span>Lumora Music</div>

  <div class="person">
    <p class="person-name">CLARE YOSHINAGA</p>
    <p class="person-role">PRESIDENT</p>
  </div>

  <ul class="contacts">
    <li>
      <svg viewBox="0 0 12 12" aria-hidden="true"><path d="M1 3c0-1 1-2 2-2h6c1 0 2 1 2 2v1H8V3H4v1H1z M2 5h8l1 6H1z M4.5 7.5a1.5 1.5 0 1 0 3 0a1.5 1.5 0 1 0-3 0"/></svg>
      0455 318 602
    </li>
    <li>
      <svg viewBox="0 0 12 12" aria-hidden="true"><path d="M3 0h6v12H3z M4 1.5v8h4v-8z"/></svg>
      0455 318 602
    </li>
    <li>
      <svg viewBox="0 0 12 12" aria-hidden="true"><path d="M0 2h12v8H0z M1 3l5 4l5-4z" fill-rule="evenodd"/></svg>
      instagram@lumoramusicevents
    </li>
  </ul>

  <div class="divider"></div>

  <address class="address" style="font-style:normal">
    Level 7, 41 Caddow Lane<br>
    Sydney, 2000<br>
    www.lumoramusicevents-demo.net
  </address>
</section>

</body>
</html>
```